Bold Website Redesign for a Disruptive Training Brand

Brightmoor Labs is a bold, no-fluff sales & leadership training company powered by AI-driven practice and behavioral science. We’ve already built our website structure and copy in Craftly.io — now we need a designer to fully transform the visual design across all pages (Home, Approach, Programs, About, Contact).
We’re looking for a modern, memorable, high-performance aesthetic that blends human energy, science, and tech without feeling corporate or safe. Clean, bold typography, fluid layout, strong emotional hero moments, subtle motion, and imagery that mixes real people with abstract scientific/tech visuals.Because our clients are primarily North American, please ensure any human photography or AI-generated imagery reflects a North American business context and demographics (modern, diverse, and realistic).

Your job is visual redesign only — no coding required.
The final design must be practical to rebuild inside Craftly.io.

A full, detailed creative brief (plus logo files) is included in the uploaded files.
If you can bring a mix of edge, intelligence, and strong visual storytelling, we’d love to see your work.

Website is already built in Craftly.io at - https://brightmoor-website-tempdesign.craftly.app — structure is set, visuals need redesign.

```html
<!DOCTYPE html>
<html lang="en">
<head>
<meta charset="utf-8">
<title>Brightmoor Labs — Training That Practices Back</title>
<link href="https://fonts.googleapis.com/css2?family=Inter:wght@400;500;600;700&display=swap" rel="stylesheet">
<style>
:root{
  --navy:#143a8c;
  --navy-deep:#0f3282;
  --ink:#0b1b4a;
  --text:#5a5f6b;
  --pale:#eff4fc;
  --band:#e3eaf8;
  --chart-light:#c3d0ea;
  --chart-dark:#809fdf;
  --white:#ffffff;
}
*{margin:0;padding:0;box-sizing:border-box}
html,body{width:1200px;height:2879px;overflow:hidden}
body{position:relative;font-family:'Inter',sans-serif;background:var(--white);color:var(--text)}
.abs{position:absolute}

/* header */
.hero{left:0;top:0;width:1200px;height:663px;background:radial-gradient(ellipse at 45% 30%,#5a4a1e 0%,transparent 35%),radial-gradient(ellipse at 85% 60%,#4d4a20 0%,transparent 30%),linear-gradient(120deg,#0a1638,#0c1c4d 55%,#081233)}
.nav{left:0;top:0;width:1200px;height:78px;background:rgba(5,12,35,.55)}
.brand{display:flex;align-items:center;gap:10px;color:var(--white);font-weight:700;font-size:16px;letter-spacing:2px}
.brand .mark{width:14px;height:14px;background:currentColor}
.nav .brand{left:84px;top:28px}
.nav-links a{position:absolute;top:30px;color:var(--white);font-size:15px;text-decoration:none}
.nav-links .active{font-weight:600}
.btn-tick{display:flex;align-items:center;background:var(--navy);color:var(--white);border-radius:0 6px 6px 0;font-weight:500;text-decoration:none}
.btn-tick .tick{background:var(--white);height:100%;display:flex;align-items:center;justify-content:center;position:relative}
.btn-tick .tick::after{content:"";position:absolute;right:-6px;top:50%;margin-top:-6px;border-left:6px solid var(--white);border-top:6px solid transparent;border-bottom:6px solid transparent}
.nav .btn-tick{left:985px;top:18px;width:146px;height:41px;font-size:16px}
.nav .btn-tick .tick{width:36px}
.nav .btn-tick span{margin-left:19px}
.eyebrow{left:69px;top:258px;color:var(--white);font-size:14px;font-weight:500}
.hero-title{left:69px;top:275px;color:var(--white);font-size:72px;line-height:88px;font-weight:500}
.hero-title b{font-weight:700}
.hero .btn-tick{left:69px;top:465px;width:246px;height:52px;font-size:19px}
.hero .btn-tick .tick{width:38px}
.hero .btn-tick span{margin-left:25px}

/* forgetting curve */
.curve-title{left:71px;top:740px;width:900px;color:var(--navy);font-size:45px;line-height:54px;font-weight:700}
.curve-copy{left:71px;top:870px;width:600px;font-size:19.5px;line-height:28px}
.btn-solid{background:var(--navy);color:var(--white);border-radius:0 14px 14px 0;display:flex;align-items:center;text-decoration:none}
.curve-btn{left:71px;top:1013px;width:582px;height:63px;font-size:22px;padding-left:31px}
.chart{left:397px;top:936px;width:734px;height:307px}
.chart-labels{left:397px;top:1251px;width:734px;display:flex;justify-content:space-between;font-size:15.5px}
.chart-labels strong{color:var(--navy);font-weight:600}

/* team */
.team-panel{left:411px;top:1341px;width:789px;height:401px;background:linear-gradient(120deg,#1d4aa3,#1a459c 60%,#234f9f)}
.team-photo{left:0;top:1382px;width:609px;height:399px;background:linear-gradient(135deg,#d9dde3,#f2f2ef 45%,#c9c3bd)}
.team-title{left:654px;top:1419px;color:var(--white);font-size:33px;line-height:38px;font-weight:600}
.team-copy{left:654px;top:1512px;width:440px;color:var(--white);font-size:14.3px;line-height:20px}
.team-panel-btn{left:654px;top:1613px;width:188px;height:42px;font-size:16.5px}
.team-panel-btn .tick{width:35px}
.team-panel-btn span{margin-left:17px}

/* pillars */
.pillars-title{left:0;top:1850px;width:1200px;text-align:center;color:var(--navy);font-size:47px;font-weight:700}
.pillars-sub{left:0;top:1911px;width:1200px;text-align:center;font-size:19px}
.card{top:1974px;width:269px;height:242px;border:1px solid #dde3ee;border-radius:46px 0 46px 0;overflow:hidden;background:var(--white);text-align:center}
.card .band{height:91px;background:var(--band)}
.card .icon{position:absolute;left:105px;top:56px;width:58px;height:58px;border-radius:50%;background:var(--navy);border:3px solid var(--white);display:flex;align-items:center;justify-content:center}
.card h3{margin-top:43px;color:var(--navy);font-size:22px;font-weight:700}
.card p{margin:12px auto 0;width:220px;font-size:12.8px;line-height:18.5px}

/* footer */
.footer-bg{left:0;top:2396px;width:1200px;height:483px;background:var(--pale)}
.cta{left:140px;top:2297px;width:919px;height:189px;background:var(--navy-deep);border-radius:56px 0 56px 0}
.cta h2{position:absolute;left:43px;top:55px;color:var(--white);font-size:33px;line-height:38px;font-weight:500}
.cta a{position:absolute;left:678px;top:74px;width:198px;height:41px;background:var(--white);color:var(--navy);border-radius:0 8px 8px 0;font-size:16px;font-weight:500;display:flex;align-items:center;justify-content:center;text-decoration:none}
.footer-brand{left:162px;top:2590px;color:var(--navy);font-size:20px}
.footer-about{left:150px;top:2663px;width:270px;font-size:14.5px;line-height:22px;color:#222}
.social{top:2742px;width:28px;height:28px;border-radius:50%;background:var(--navy)}
.col h4{color:var(--navy);font-size:18px;font-weight:700;letter-spacing:1px;margin-bottom:18px}
.col li{list-style:none;font-size:15px;color:#333;height:37.4px}
.col.contact li{display:flex;gap:8px;line-height:19px}
.col.contact svg{flex:none;margin-top:3px}
.arc{left:0;top:2810px;width:1200px;height:69px}
.copyright{left:0;top:2843px;width:1200px;text-align:center;color:var(--white);font-size:15.5px}
</style>
</head>
<body>

<section class="abs hero" role="img" aria-label="Glowing DNA double helix made of connected data points on a dark navy background"></section>

<header class="abs nav">
  <div class="abs brand"><span class="mark"></span>BRIGHTMOOR LABS</div>
  <nav class="nav-links">
    <a class="active" style="left:438px">Home</a>
    <a style="left:535px">Approach</a>
    <a style="left:658px">Programs</a>
    <a style="left:781px">About</a>
    <a style="left:878px">Contact</a>
  </nav>
  <a class="abs btn-tick"><span class="tick"><svg width="16" height="16" viewBox="0 0 16 16"><circle cx="8" cy="8" r="7" fill="none" stroke="#222" stroke-width="1.3"/><path d="M5 8.2l2 2 4-4" fill="none" stroke="#222" stroke-width="1.3"/></svg></span><span>Let's Talk</span></a>
</header>

<p class="abs eyebrow">AI-DRIVEN SUSTAINMENT THAT BUILDS MASTERY — SO YOU DON'T HAVE TO.</p>
<h1 class="abs hero-title"><b>TRAINING THAT</b><br>Practices Back.</h1>
<a class="abs btn-tick" style="left:69px;top:465px;width:246px;height:52px;font-size:19px"><span class="tick" style="width:38px"><svg width="20" height="20" viewBox="0 0 16 16"><circle cx="8" cy="8" r="7" fill="none" stroke="#222" stroke-width="1.2"/><path d="M5 8.2l2 2 4-4" fill="none" stroke="#222" stroke-width="1.2"/></svg></span><span style="margin-left:25px">See How We Do It</span></a>

<h2 class="abs curve-title">The Real Problem Isn't Your People — It's The Forgetting Curve.</h2>
<p class="abs curve-copy">Within a week, most training disappears. Leaders are left guessing who's using what they learned — and no one has time to fix it. We built Brightmoor Labs to make progress automatic, measurable, and real.</p>
<a class="abs btn-solid curve-btn">Watch how sustained practice changes the curve</a>

<svg class="abs chart" viewBox="0 0 657 275" preserveAspectRatio="none">
  <g fill="var(--chart-light)">
    <rect x="0" y="266" width="55" height="9"/>
    <rect x="55" y="251" width="55" height="24"/>
    <rect x="110" y="215" width="55" height="60"/>
    <rect x="165" y="202" width="55" height="73"/>
    <rect x="220" y="183" width="55" height="92"/>
    <rect x="275" y="175" width="55" height="100"/>
    <rect x="330" y="162" width="55" height="113"/>
    <rect x="385" y="125" width="55" height="150"/>
    <rect x="440" y="90" width="55" height="185"/>
    <rect x="495" y="60" width="55" height="215"/>
    <rect x="550" y="23" width="55" height="252"/>
    <rect x="605" y="0" width="52" height="275"/>
  </g>
  <g fill="var(--chart-dark)">
    <rect x="0" y="270" width="55" height="5"/>
    <rect x="55" y="268" width="55" height="7"/>
    <rect x="110" y="265" width="55" height="10"/>
    <rect x="165" y="255" width="55" height="20"/>
    <rect x="220" y="243" width="55" height="32"/>
    <rect x="275" y="213" width="55" height="62"/>
    <rect x="330" y="193" width="55" height="82"/>
    <rect x="385" y="183" width="55" height="92"/>
    <rect x="440" y="150" width="55" height="125"/>
    <rect x="495" y="100" width="55" height="175"/>
    <rect x="550" y="100" width="55" height="175"/>
    <rect x="605" y="60" width="52" height="215"/>
  </g>
  <rect x="0" y="273" width="657" height="2" fill="var(--chart-dark)"/>
</svg>
<div class="abs chart-labels"><span>Within a week, 70% is gone.</span><strong>We built the fix in.</strong><span>People forget fast.</span></div>

<div class="abs team-panel"></div>
<div class="abs team-photo" role="img" aria-label="Diverse team of colleagues reviewing documents and a tablet together around an office table"></div>
<h2 class="abs team-title">Built By People Who've Led<br>The Change Themselves.</h2>
<p class="abs team-copy">Behind Brightmoor Labs are leaders who've lived the challenge of making learning last. They've scaled companies, built cultures, and led transformation — and now they've designed the system they always wished existed.</p>
<a class="abs btn-tick team-panel-btn"><span class="tick"><svg width="16" height="16" viewBox="0 0 16 16"><circle cx="8" cy="8" r="7" fill="none" stroke="#222" stroke-width="1.3"/><path d="M5 8.2l2 2 4-4" fill="none" stroke="#222" stroke-width="1.3"/></svg></span><span>Meet The Team</span></a>

<h2 class="abs pillars-title">Practice Made Permanent.</h2>
<p class="abs pillars-sub">You'll replace "hope they remember" with a system that makes sure they do.</p>

<article class="abs card" style="left:142px">
  <div class="band"></div>
  <div class="icon"><svg width="24" height="24" viewBox="0 0 24 24" fill="none" stroke="#fff" stroke-width="1.6"><path d="M2 9l10-5 10 5-10 5z"/><path d="M6 11v5c3 3 9 3 12 0v-5"/></svg></div>
  <h3>LEARN</h3>
  <p>Fast, focused workshops, built on science, that install the mindset and skills that matter most.</p>
</article>
<article class="abs card" style="left:465px">
  <div class="band"></div>
  <div class="icon"><svg width="26" height="26" viewBox="0 0 24 24" fill="none" stroke="#fff" stroke-width="1.6"><path d="M12 2l2.6 2 3.3-.2.9 3.2 2.7 1.9-1.2 3.1 1.2 3.1-2.7 1.9-.9 3.2-3.3-.2L12 22l-2.6-2-3.3.2-.9-3.2-2.7-1.9L3.7 12 2.5 8.9l2.7-1.9.9-3.2 3.3.2z"/><path d="M8 12l3 3 5-6"/></svg></div>
  <h3>CERTIFY</h3>
  <p>Programmatic AI-driven practice and feedback - mastery without management overhead.</p>
</article>
<article class="abs card" style="left:788px">
  <div class="band"></div>
  <div class="icon"><svg width="24" height="24" viewBox="0 0 24 24" fill="none" stroke="#fff" stroke-width="1.5"><path d="M20 12a8 8 0 0 1-13.7 5.6M4 12a8 8 0 0 1 13.7-5.6"/><path d="M18 3v4h-4M6 21v-4h4"/><path d="M13 7l-3 5h4l-3 5"/></svg></div>
  <h3>SUSTAIN</h3>
  <p>Light-touch challenges and dashboards that keep skills sharp long after training ends.</p>
</article>

<div class="abs footer-bg"></div>
<section class="abs cta">
  <h2>Ready to see what lasting<br>capability looks like?</h2>
  <a>Start a Conversation</a>
</section>

<div class="abs brand footer-brand"><span class="mark"></span>BRIGHTMOOR LABS</div>
<p class="abs footer-about">Making learning that sticks through AI-driven sustainment and behavioral science.</p>
<span class="abs social" style="left:149px"></span>
<span class="abs social" style="left:188px"></span>

<div class="abs col" style="left:474px;top:2560px">
  <h4>QUICK</h4>
  <ul><li>Home</li><li>Approach</li><li>Programs</li><li>About</li><li>Contact</li></ul>
</div>
<div class="abs col" style="left:633px;top:2560px">
  <h4>PERMANENT</h4>
  <ul><li>Learn</li><li>Certify</li><li>Sustain</li></ul>
</div>
<div class="abs col contact" style="left:828px;top:2560px">
  <h4>GET IN TOUCH</h4>
  <ul>
    <li><svg width="12" height="12" viewBox="0 0 12 12"><rect x="0" y="2" width="12" height="8" rx="1" fill="var(--navy)"/><path d="M0.5 2.5l5.5 4 5.5-4" fill="none" stroke="#fff" stroke-width="1"/></svg>contact@brightmoorlabs.com</li>
    <li><svg width="12" height="12" viewBox="0 0 12 12"><path d="M2 1l2.5 0 1 3-1.5 1c.8 1.5 1.7 2.4 3 3l1-1.5 3 1V11c-5 0-9-4-9-9z" fill="var(--navy)"/></svg>+1 (555) 014-2290</li>
    <li><svg width="12" height="14" viewBox="0 0 12 14"><path d="M6 0a5 5 0 0 1 5 5c0 3.5-5 9-5 9S1 8.5 1 5a5 5 0 0 1 5-5z" fill="var(--navy)"/><circle cx="6" cy="5" r="1.8" fill="#fff"/></svg>4820 Harlow Ave Suite 210<br>Riverton, AZ 85099</li>
  </ul>
</div>

<svg class="abs arc" viewBox="0 0 1200 69" preserveAspectRatio="none"><path d="M0 69 Q600 -40 1200 69z" fill="var(--navy-deep)"/></svg>
<p class="abs copyright">© 2025 Brightmoor Labs. All rights Reserved.</p>

</body>
</html>
```